Two Day Training Event includes a Dinner/Bowling Party at Larkspur in Troy, MI

I would like a postcard to attract Insurance Agents to an QWT meeting calling it a summit or something like that. Just something to mail to insurance agents telling them about our upcoming event with over 20 carriers. An opportunity to certify face to face with MAPD carriers and see what 2020 has to offer. Prior to OEP OPen Enrollment and AEP Annual Election period we have a number of meetings. Carriers want to come especially if we can get a number of agents. We are going to go to Larkspur a fun bowling alley for dinner, drinks and bowling to network and talk about the upcoming year.

Target Market(s)

Existing and new insurance agents

Industry/Entity Type

Insurance Broker

Contact Information for Business Card

Looking for a new card design I sent my LOGO and can upload my existing card.

Font styles to use
Serif

Colors

Designer to choose colors to be used in the design.

Requirements
Must have
• Dates Sept 16 and 17th
• location Harrowgate Conference Hall in Ridgeford
• times
Nice to have
• It would be nice to see a fun design.

```html
<!DOCTYPE html>
<html lang="en">
<head>
<meta charset="utf-8">
<title>QWT Meeting Calling Postcard</title>
<link href="https://fonts.googleapis.com/css2?family=Montserrat:wght@500;600;700;800;900&display=swap" rel="stylesheet">
<style>
  :root{
    --navy:#1b2a7a;
    --navy-deep:#101b58;
    --blue:#1f4fc4;
    --orange:#f6a21a;
    --orange-deep:#ee8a12;
    --ink:#1d1d2b;
    --paper:#ffffff;
    --backdrop:#eceef2;
    --rule:#c9ccd6;
  }
  *{box-sizing:border-box;margin:0;padding:0}
  html,body{width:690px;height:1200px;overflow:hidden}
  body{background:var(--backdrop);font-family:"Montserrat",Arial,sans-serif;color:var(--ink);position:relative}
  .postcard{position:absolute;left:35px;width:620px;height:413px;background:var(--paper);overflow:hidden;box-shadow:0 6px 18px rgba(20,30,60,.18)}
  .postcard--front{top:150px}
  .postcard--back{top:640px}

  /* front */
  .front-title{position:absolute;left:34px;top:40px;font-weight:900;font-size:92px;line-height:.9;color:var(--navy);letter-spacing:-2px}
  .front-sub{position:absolute;left:38px;top:128px;font-weight:800;font-size:25px;color:var(--orange-deep)}
  .carriers{position:absolute;left:38px;top:170px;background:var(--navy);color:#fff;font-weight:800;font-size:23px;padding:8px 16px;letter-spacing:.5px}
  .carriers em{font-style:normal;color:var(--orange);font-size:30px}
  .event-date{position:absolute;left:38px;top:228px;font-weight:800;font-size:17px;color:var(--navy)}
  .event-place{position:absolute;left:38px;top:254px;font-weight:600;font-size:12.5px;color:var(--navy);line-height:1.35;width:200px}
  .icon{display:inline-block;vertical-align:-2px;margin-right:5px}
  .photo-ring{position:absolute;left:312px;top:22px;width:230px;height:230px}
  .photo{position:absolute;left:340px;top:50px;width:174px;height:174px;border-radius:50%;background:radial-gradient(circle at 45% 40%,#b9c2cf,#5f6b7e 70%,#3a4354)}
  .confetti{position:absolute;right:0;top:0;width:130px;height:300px;background:linear-gradient(160deg,rgba(246,162,26,.55),rgba(231,70,120,.35) 40%,rgba(70,170,230,.3) 70%,rgba(255,255,255,0));}
  .invite-bar{position:absolute;left:38px;top:316px;width:270px;background:var(--orange);color:var(--navy-deep);font-weight:700;font-size:9.5px;line-height:1.35;padding:7px 10px}
  .brand{position:absolute;display:flex;align-items:center;gap:8px;color:var(--navy)}
  .brand-name{font-weight:900;font-size:34px;letter-spacing:-.5px}
  .brand-tag{font-weight:600;font-size:10px;line-height:1.2;width:78px}
  .postcard--front .brand{left:388px;top:338px}

  /* back */
  .back-panel{position:absolute;left:0;top:0;width:310px;height:413px}
  .back-title{position:absolute;left:30px;top:96px;font-weight:900;font-size:62px;line-height:.9;color:#fff;letter-spacing:-1px}
  .back-sub{position:absolute;left:32px;top:156px;font-weight:800;font-size:17px;color:var(--orange)}
  .perks{position:absolute;left:32px;top:200px;width:220px;list-style:none;color:#fff;font-weight:600;font-size:11px;line-height:1.35}
  .perks li{position:relative;padding-left:16px;margin-bottom:12px}
  .perks li::before{content:"";position:absolute;left:0;top:4px;width:8px;height:8px;background:var(--orange);border-radius:50%}
  .postcard--back .brand{left:352px;top:32px}
  .stamp-box{position:absolute;right:28px;top:28px;width:62px;height:72px;border:2px solid var(--rule)}
  .address-lines{position:absolute;left:408px;top:206px;width:180px}
  .address-lines span{display:block;height:1px;background:var(--rule);margin-bottom:30px}
  .web{position:absolute;right:28px;bottom:22px;font-weight:700;font-size:12px;color:var(--navy)}
</style>
</head>
<body>

<section class="postcard postcard--front">
  <div class="confetti" role="img" aria-label="Colourful party confetti"></div>
  <svg class="photo-ring" viewBox="0 0 230 230" aria-hidden="true">
    <circle cx="115" cy="115" r="100" fill="none" stroke="var(--orange)" stroke-width="24" stroke-dasharray="520 40 60 20"/>
  </svg>
  <div class="photo" role="img" aria-label="Photo of agents meeting around a conference table"></div>

  <h1 class="front-title">QWT</h1>
  <p class="front-sub">MEETING CALLING</p>
  <p class="carriers">OVER <em>20</em> CARRIERS</p>
  <p class="event-date">
    <svg class="icon" width="14" height="14" viewBox="0 0 14 14"><rect x="1" y="2" width="12" height="11" rx="1" fill="none" stroke="var(--orange-deep)" stroke-width="1.6"/><line x1="1" y1="5.5" x2="13" y2="5.5" stroke="var(--orange-deep)" stroke-width="1.6"/></svg>16<sup>th</sup> and 17<sup>th</sup> SEPT 2019
  </p>
  <p class="event-place">
    <svg class="icon" width="11" height="14" viewBox="0 0 11 14"><path d="M5.5 13.5S1 8.4 1 5.3a4.5 4.5 0 0 1 9 0c0 3.1-4.5 8.2-4.5 8.2z" fill="var(--orange-deep)"/><circle cx="5.5" cy="5.3" r="1.6" fill="#fff"/></svg>Harrowgate Conference Hall<br>in Ridgeford
  </p>
  <p class="invite-bar">Join us at Larkspur for dinner, drinks and bowling to network and talk about the upcoming year.</p>

  <div class="brand">
    <span class="brand-name">QWT</span>
    <span class="brand-tag">Quorum Wellness Trust</span>
  </div>
</section>

<section class="postcard postcard--back">
  <svg class="back-panel" viewBox="0 0 310 413" aria-hidden="true">
    <defs>
      <linearGradient id="panelBlue" x1="0" y1="0" x2="1" y2="1">
        <stop offset="0" stop-color="#2b5fd6"/>
        <stop offset="1" stop-color="#13206a"/>
      </linearGradient>
    </defs>
    <path d="M0 0H250C300 90 320 230 285 413H0Z" fill="url(#panelBlue)"/>
    <path d="M250 0C300 90 320 230 285 413H305C338 230 318 90 272 0Z" fill="var(--orange)"/>
  </svg>
  <h2 class="back-title">QWT</h2>
  <p class="back-sub">MEETING CALLING</p>
  <ul class="perks">
    <li>An opportunity to certify face to face with MAPD carriers</li>
    <li>See what 2020 has to offer</li>
    <li>Prior to OEP Open Enrollment and AEP Annual Election period</li>
  </ul>

  <div class="brand">
    <span class="brand-name">QWT</span>
    <span class="brand-tag">Quorum Wellness Trust</span>
  </div>
  <div class="stamp-box"></div>
  <div class="address-lines"><span></span><span></span><span></span><span></span></div>
  <p class="web">qwtplans.com</p>
</section>

</body>
</html>
```